Boutique Wealth management firm needs a new business card design

I want to update my business card design to be more consistent with the look and feel of my website (www.brisvane-wealth.com). I would like to incorporate an ivory parchment background and am open to switching from the current "portrait" layout to a more traditional "landscape" orientation. The final design should convey stability and exclusivity and I want something in PDF format that is ready to send to the printer

Thank you all for taking the time to submit your designs for my project. I've made my decision and picked the design I like best. Thanks again!

```html
<!DOCTYPE html>
<html lang="en">
<head>
<meta charset="utf-8">
<title>Brisvane Wealth Advisory – Business Card</title>
<link rel="stylesheet" href="https://fonts.googleapis.com/css2?family=Arimo:wght@400;700&display=swap">
<style>
  :root {
    --backdrop: #2f3833;
    --parchment: #f4ecd2;
    --parchment-light: #f8f2de;
    --parchment-mottle: #e9dcb6;
    --parchment-edge: #e3d4aa;
    --maroon: #6a1630;
    --band: #3a0d19;
    --ink: #1c1c1c;
    --slate: #4b5866;
    --gold: #d8aa4c;
  }
  html, body {
    margin: 0;
    width: 1200px;
    height: 1000px;
    overflow: hidden;
    background: var(--backdrop);
    font-family: "Arimo", Arial, sans-serif;
  }
  .card {
    position: absolute;
    left: 100px;
    top: 214px;
    width: 1000px;
    height: 572px;
    background:
      radial-gradient(ellipse 220px 140px at 18% 22%, var(--parchment-mottle), transparent 70%),
      radial-gradient(ellipse 260px 160px at 72% 30%, var(--parchment-light), transparent 70%),
      radial-gradient(ellipse 200px 120px at 55% 62%, var(--parchment-mottle), transparent 70%),
      radial-gradient(ellipse 240px 150px at 88% 70%, var(--parchment-mottle), transparent 70%),
      radial-gradient(ellipse 180px 110px at 30% 58%, var(--parchment-light), transparent 70%),
      radial-gradient(ellipse at 45% 40%, var(--parchment) 0%, var(--parchment) 55%, var(--parchment-edge) 100%);
    box-shadow: 0 14px 40px rgba(0,0,0,0.45);
    overflow: hidden;
  }
  .card-texture {
    position: absolute;
    inset: 0;
  }
  .brand {
    position: absolute;
    right: 60px;
    top: 92px;
    display: flex;
    align-items: center;
    gap: 18px;
    color: var(--maroon);
    font-size: 50px;
    font-weight: 700;
    line-height: 1;
    white-space: nowrap;
  }
  .brand-mark {
    width: 30px;
    height: 30px;
    background: var(--maroon);
  }
  .person {
    position: absolute;
    right: 150px;
    top: 238px;
    text-align: center;
  }
  .person-name {
    font-size: 44px;
    font-weight: 700;
    color: var(--ink);
    margin: 0;
  }
  .person-name sup { font-size: 24px; }
  .person-title {
    font-size: 26px;
    font-weight: 700;
    color: var(--slate);
    margin: 6px 0 0;
  }
  .mailing {
    position: absolute;
    left: 56px;
    top: 336px;
    font-size: 30px;
    line-height: 1.22;
    color: var(--ink);
    text-align: center;
  }
  .divider {
    position: absolute;
    left: 468px;
    top: 340px;
    width: 4px;
    height: 112px;
    background: var(--maroon);
  }
  .contact {
    position: absolute;
    left: 500px;
    top: 342px;
    font-size: 30px;
    line-height: 1.22;
    color: var(--ink);
  }
  .band {
    position: absolute;
    left: 0;
    bottom: 0;
    width: 100%;
    height: 84px;
    background: var(--band);
  }
  .license {
    position: absolute;
    left: 60px;
    top: 24px;
    font-size: 28px;
    color: var(--gold);
  }
</style>
</head>
<body>
  <div class="card">
    <div class="card-texture" role="img" aria-label="Ivory parchment paper texture"></div>
    <div class="brand">
      <span class="brand-mark"></span>
      <span class="brand-name">Brisvane Wealth Advisory</span>
    </div>
    <div class="person">
      <p class="person-name">Dale Harmon, CFP<sup>®</sup></p>
      <p class="person-title">Principal</p>
    </div>
    <div class="mailing">
      Mailing Address:<br>
      2870 Oakmont Ave. #412<br>
      Fairbrook, CA 94500
    </div>
    <div class="divider"></div>
    <div class="contact">
      925-555-0148<br>
      dale@brisvane-wealth.com<br>
      www.brisvane-wealth.com
    </div>
    <div class="band">
      <span class="license">CA Insurance License #0K58213</span>
    </div>
  </div>
</body>
</html>
```